DPM Marketing Postcard

Design a 2 Sided marketing postcard for our Real estate management caompany. Looking for a professional yet fresh look that will be printed on a 6"x9" glossy flier

Contact information is www.dunkeldmanagement-example.com dunkeldmanagement@dunkeldmail-example.com and 312-480-7193

WE are targeting small condo and town home properties to take on their administrative responsibilities of management

```html
<!DOCTYPE html>
<html lang="en">
<head>
<meta charset="utf-8">
<title>DPM Marketing Postcard</title>
<link rel="stylesheet" href="https://fonts.googleapis.com/css2?family=Ubuntu:ital,wght@0,400;0,500;0,700;1,500&family=Didact+Gothic&display=swap">
<style>
  :root {
    --page: #e9ecef;
    --blue: #1f86cf;
    --blue-dark: #1567a6;
    --blue-light: #3fa3e3;
    --black: #151515;
    --orange: #f08a1c;
    --orange-dark: #e06d0f;
    --ink: #3b3f44;
    --rule: #d3d9df;
    --white: #ffffff;
  }
  * { box-sizing: border-box; margin: 0; padding: 0; }
  html, body { width: 800px; height: 1200px; overflow: hidden; }
  body {
    background: var(--page);
    font-family: "Didact Gothic", "Century Gothic", sans-serif;
    color: var(--ink);
    position: relative;
  }
  .card {
    position: absolute;
    left: 40px;
    width: 720px;
    height: 480px;
    background: var(--white);
    box-shadow: 0 3px 10px rgba(0,0,0,.25);
    overflow: hidden;
  }
  .card--front { top: 90px; }
  .card--back { top: 630px; }

  .title-band {
    position: absolute;
    left: 10px; right: 10px; top: 10px;
    height: 48px;
    background: linear-gradient(180deg, var(--blue-light), var(--blue) 55%, var(--blue-dark));
    color: var(--white);
    font-family: "Ubuntu", sans-serif;
    font-weight: 700;
    font-size: 22px;
    letter-spacing: .2px;
    display: flex; align-items: center;
    padding-left: 44px;
  }
  .title-band .abbr { font-weight: 400; margin-left: 6px; }

  /* front */
  .front-photo {
    position: absolute; left: 10px; right: 10px; top: 58px; bottom: 10px;
    background: linear-gradient(135deg, #cfd6dd 0%, #f1f3f5 40%, #b9a79a 75%, #e7e9ec 100%);
  }
  .tagline {
    position: absolute; left: 10px; right: 10px; top: 58px; height: 22px;
    background: var(--black);
    color: var(--white);
    font-family: "Ubuntu", sans-serif;
    font-style: italic; font-weight: 500;
    font-size: 13px;
    display: flex; align-items: center; justify-content: center;
  }
  .panel {
    position: absolute; left: 36px; right: 30px; top: 82px; bottom: 34px;
    display: grid; grid-template-columns: 1fr 1fr;
    background: rgba(255,255,255,.82);
  }
  .col { display: flex; flex-direction: column; }
  .col + .col { border-left: 1px solid var(--rule); }
  .col-head {
    height: 28px; flex: none;
    background: linear-gradient(180deg, var(--blue-light), var(--blue));
    color: var(--white);
    font-family: "Ubuntu", sans-serif; font-weight: 700; font-size: 15px;
    display: flex; align-items: center; justify-content: center;
  }
  .col-head--mixed { text-transform: none; }
  .points { list-style: none; display: flex; flex-direction: column; flex: 1; }
  .points li {
    flex: 1;
    position: relative;
    font-size: 10.5px; line-height: 1.3;
    padding: 6px 14px 6px 22px;
    border-bottom: 1px solid var(--rule);
    display: flex; align-items: center;
  }
  .points li:last-child { border-bottom: none; }
  .points li::before {
    content: ""; position: absolute; left: 10px; top: 11px;
    width: 5px; height: 5px; border-radius: 50%; background: var(--orange);
  }
  .points em { font-style: italic; }
  .contact-tab {
    position: absolute; bottom: 10px; left: 160px; width: 400px; height: 22px;
    background: var(--orange);
    clip-path: polygon(4% 0, 96% 0, 100% 100%, 0 100%);
    color: var(--white); font-size: 11px;
    display: flex; align-items: center; justify-content: center; gap: 6px;
  }
  .contact-tab svg { width: 11px; height: 11px; }

  /* back */
  .back-list {
    position: absolute; left: 22px; top: 76px; width: 300px;
    list-style: none;
  }
  .back-list li {
    position: relative;
    font-size: 12.5px; line-height: 1.3;
    padding-left: 16px; margin-bottom: 12px;
  }
  .back-list li::before {
    content: ""; position: absolute; left: 2px; top: 6px;
    width: 5px; height: 5px; border-radius: 50%; background: var(--orange);
  }
  .back-art { position: absolute; left: 0; top: 0; width: 720px; height: 480px; }
  .phone-box {
    position: absolute; left: 10px; bottom: 10px; width: 300px; height: 66px;
    background: linear-gradient(180deg, var(--orange), var(--orange-dark));
    color: var(--white);
    padding: 10px 0 0 14px;
  }
  .phone-box .number {
    font-family: "Ubuntu", sans-serif; font-weight: 500; font-size: 27px;
    display: flex; align-items: center; gap: 12px; line-height: 1;
  }
  .phone-box .number svg { width: 24px; height: 24px; }
  .phone-box .web {
    font-size: 10.5px; margin-top: 6px; display: flex; align-items: center; gap: 6px;
  }
  .phone-box .web svg { width: 12px; height: 12px; }
</style>
</head>
<body>

<section class="card card--front" aria-label="Postcard front">
  <div class="front-photo" role="img" aria-label="Soft faded photo of an office desk with papers and a pen"></div>
  <header class="title-band">DUNKELD PROPERTY MANAGEMENT LLC <span class="abbr">(“DPM”)</span></header>
  <div class="tagline">Improve compliance, reporting, and communication amongst all owners and board members</div>

  <div class="panel">
    <div class="col">
      <h2 class="col-head">WHO WE ARE</h2>
      <ul class="points">
        <li>A professional services organization with a focus on small (3-10 unit) residential buildings</li>
        <li>Over 30 years of combined experience in real estate and property management</li>
        <li>Professional, courteous, timely service that is technologically driven</li>
      </ul>
      <h2 class="col-head col-head--mixed">Why use DPM?</h2>
      <ul class="points">
        <li>Owners are rarely suited to manage associations and the burden often falls unfairly on one or two individuals to do all the work</li>
        <li>Low monthly fees tailored to your needs</li>
        <li>The association’s board of directors maintains control of all decision making</li>
        <li></li>
      </ul>
    </div>
    <div class="col">
      <h2 class="col-head">WHAT WE DO</h2>
      <ul class="points">
        <li>Remove the administrative burden of managing small residential buildings</li>
        <li>Utilize economies of scale to reduce expenses for all owners across a wide variety of service providers</li>
        <li>Collect all assessments and pay all bills</li>
        <li>Provide monthly accounting reconciliation and reporting</li>
        <li><span>Provide access to DPM’s client portal with a central repository of all association materials <em>(bylaws, financials, meeting minutes, communications, etc)</em></span></li>
        <li>Issue 1099s to all contractors as required by law</li>
        <li>Prepare year-end financial statements</li>
        <li>Lender and legal HOA documents for mortgage companies and sales</li>
      </ul>
    </div>
  </div>

  <div class="contact-tab">
    <svg viewBox="0 0 12 12" aria-hidden="true"><circle cx="6" cy="6" r="5" fill="none" stroke="#fff" stroke-width="1.2"/><circle cx="6" cy="6" r="2" fill="#fff"/></svg>
    <span>www.dunkeldmanagement-example.com | 312-480-7193</span>
  </div>
</section>

<section class="card card--back" aria-label="Postcard back">
  <svg class="back-art" viewBox="0 0 720 480" aria-hidden="true">
    <polygon points="690,66 710,66 710,470 656,470" fill="#1f86cf"/>
  </svg>
  <svg class="back-art" viewBox="0 0 720 480" role="img" aria-label="Photo of a green lawn and trees in front of a brick residential building under a blue sky">
    <defs>
      <linearGradient id="scene" x1="0" y1="0" x2="0" y2="1">
        <stop offset="0" stop-color="#4f8fd0"/>
        <stop offset=".35" stop-color="#c9dcef"/>
        <stop offset=".55" stop-color="#4c8a2e"/>
        <stop offset="1" stop-color="#6fbf2c"/>
      </linearGradient>
    </defs>
    <polygon points="372,66 685,66 650,470 330,470" fill="url(#scene)"/>
  </svg>
  <header class="title-band">DUNKELD PROPERTY MANAGEMENT LLC <span class="abbr">(“DPM”)</span></header>

  <ul class="back-list">
    <li>Cost effective property management solution for 3-10 unit buildings</li>
    <li>Prices starting as low as $100/month</li>
    <li>Utilize our economies of scale to reduce costs across existing services (trash, insurance, maintenance, etc)</li>
    <li>Eliminate the unfair burden placed on a few owners to do all the work while others free-ride</li>
    <li>Improve communication amongst all owners and board members</li>
    <li>The association’s board of directors maintain all decision-making power</li>
    <li>Utilize our vetted service providers for prompt job completion and fair pricing</li>
  </ul>

  <div class="phone-box">
    <div class="number">
      <svg viewBox="0 0 24 24" aria-hidden="true"><path d="M6.6 10.8a15.1 15.1 0 0 0 6.6 6.6l2.2-2.2a1 1 0 0 1 1-.25 11.4 11.4 0 0 0 3.6.57 1 1 0 0 1 1 1V20a1 1 0 0 1-1 1A17 17 0 0 1 3 4a1 1 0 0 1 1-1h3.5a1 1 0 0 1 1 1c0 1.25.2 2.45.57 3.57a1 1 0 0 1-.25 1z" fill="none" stroke="#fff" stroke-width="1.6"/></svg>
      <span>312-480-7193</span>
    </div>
    <div class="web">
      <svg viewBox="0 0 12 12" aria-hidden="true"><circle cx="6" cy="6" r="5" fill="none" stroke="#fff" stroke-width="1.2"/><circle cx="6" cy="6" r="2" fill="#fff"/></svg>
      <span>www.dunkeldmanagement-example.com</span>
    </div>
  </div>
</section>

</body>
</html>
```